Website Design for NimbusOps as a Service

We are building a service to allow customers to own their own private clouds easily and cheaply. Owning your own private cloud saves costs, and offers more flexibility than a public cloud provider but has historically been a complex and expensive option.

We plan to offer a service where we build and maintain your own private cloud on your own hardware for a cheap monthly costs. Similar to this service - https://stackorra.com/solutions/private-cloud

We already have a logo and branding in place - we'd like a website design to be tailored from this branding, see attached logo design.

Feel free to add important elements on the home page such as testimonials, client/partner logos, contact form, social media, etc using placeholder contents in addition to the document we attached.

We also plan to add sub-pages in the future so please make sure that your website design has a full navigation menu.

An example of the site we like: https://www.verimoxa.com/ we'd be happy for you to take inspiration from this website.

Target Market(s)

B2B focused, we are targeting start-up/small/medium sized companies who needs help with their cloud and IT infrastructure.

Industry/Entity Type

IT

Number of Pages Required

1 page

Font styles to use
Other font styles liked:
• Please refer to the attachment - font must have Mayeka Demi Bold & Retroica

Requirements
Must have
• Please add placeholder menu since we're planning to have subpages later on.

```html
<!DOCTYPE html>
<html lang="en">
<head>
<meta charset="utf-8">
<title>NimbusOps – Home (Hero Section)</title>
<link href="https://fonts.googleapis.com/css2?family=Comfortaa:wght@500;600;700&family=Poppins:wght@400;500;600;700&family=Roboto:wght@400&display=swap" rel="stylesheet">
<style>
  :root{
    --board:#ffffff;
    --stripe:#d7eaf5;
    --brand-blue:#2592d3;
    --brand-grey:#666a70;
    --navy-top:#0c1f57;
    --navy-deep:#080f45;
    --grid-blue:#1a4fb8;
    --white:#ffffff;
    --illus-a:#6b5fd6;
    --illus-b:#28b6c9;
  }
  *{margin:0;padding:0;box-sizing:border-box}
  html,body{width:1200px;height:1200px;overflow:hidden;background:var(--board)}
  .board{position:relative;width:1200px;height:1200px;background:var(--board);font-family:"Poppins",sans-serif}
  .stripes{position:absolute;inset:0}
  .brand-mark{position:absolute;left:0;right:0;top:88px;display:flex;justify-content:center;align-items:center;gap:18px}
  .brand-mark .dot{width:70px;height:70px;border-radius:50%;background:var(--brand-blue)}
  .brand-mark .name{font-family:"Poppins",sans-serif;font-weight:600;font-size:56px;color:var(--brand-grey);letter-spacing:-1px}
  .board-title{position:absolute;left:0;right:0;top:206px;text-align:center;font-family:"Comfortaa",sans-serif;font-weight:700;font-size:42px;color:var(--brand-blue)}
  .screen{position:absolute;left:133px;top:391px;width:934px;height:525px;background:linear-gradient(180deg,var(--navy-top) 0%,var(--navy-deep) 55%,#0a2a86 100%);box-shadow:0 10px 40px rgba(0,0,0,.18);overflow:hidden;color:var(--white)}
  .screen .floor{position:absolute;left:0;right:0;bottom:0;height:170px;background:linear-gradient(180deg,rgba(26,79,184,0) 0%,rgba(26,79,184,.55) 100%)}
  .announce{height:34px;background:var(--brand-blue);display:flex;align-items:center;padding-left:60px;font-size:11px;gap:9px}
  .announce .close{position:absolute;right:62px;top:9px}
  .nav{position:absolute;top:48px;left:60px;right:60px;height:41px;display:flex;align-items:center}
  .nav .logo{display:flex;align-items:center;gap:7px;width:222px}
  .nav .logo .dot{width:26px;height:26px;border-radius:50%;background:var(--brand-blue)}
  .nav .logo .name{font-weight:600;font-size:20px;color:var(--brand-blue);letter-spacing:-.3px}
  .nav ul{list-style:none;display:flex;gap:20px;font-size:10.5px;font-weight:600}
  .nav .search{position:absolute;left:667px;top:13px}
  .btn{display:inline-flex;align-items:center;justify-content:center;height:41px;font-weight:600;font-size:13px;color:var(--white)}
  .btn-solid{background:var(--brand-blue)}
  .btn-ghost{border:1.5px solid var(--brand-blue)}
  .nav .btn{position:absolute;left:705px;width:109px}
  .hero-title{position:absolute;left:50px;top:159px;width:450px;font-family:"Comfortaa",sans-serif;font-weight:600;font-size:21.5px;line-height:27px;color:var(--brand-blue)}
  .hero-lead{position:absolute;left:52px;top:255px;width:370px;font-weight:700;font-size:12.6px;line-height:13.7px}
  .hero-text{position:absolute;left:50px;top:321px;width:420px;font-family:"Roboto",sans-serif;font-size:12.5px;line-height:15.5px}
  .hero-actions{position:absolute;left:50px;top:379px;display:flex;gap:14px}
  .hero-actions .btn-solid{width:109px}
  .hero-actions .btn-ghost{width:120px}
  .hero-illustration{position:absolute;left:506px;top:156px;width:348px;height:287px;border-radius:14px;background:radial-gradient(ellipse at 55% 50%,rgba(107,95,214,.55) 0%,rgba(40,182,201,.18) 55%,rgba(12,31,87,0) 78%)}
  .chat{position:absolute;left:863px;top:414px;width:44px;height:44px;border-radius:50%;background:var(--brand-blue);display:flex;align-items:center;justify-content:center}
</style>
</head>
<body>
<div class="board">
  <svg class="stripes" width="1200" height="1200" viewBox="0 0 1200 1200" aria-hidden="true">
    <g stroke="var(--stripe)" stroke-width="3">
      <line x1="314" y1="0" x2="-748" y2="1200"/>
      <line x1="669" y1="0" x2="-393" y2="1200"/>
      <line x1="1025" y1="0" x2="-37" y2="1200"/>
      <line x1="1380" y1="0" x2="318" y2="1200"/>
      <line x1="1735" y1="0" x2="673" y2="1200"/>
      <line x1="2090" y1="0" x2="1028" y2="1200"/>
    </g>
  </svg>

  <div class="brand-mark"><span class="dot"></span><span class="name">NimbusOps</span></div>
  <h1 class="board-title">Home (Hero Section)</h1>

  <section class="screen">
    <div class="floor"></div>
    <div class="announce">
      <svg width="16" height="13" viewBox="0 0 16 13" fill="none" stroke="#fff" stroke-width="1.3"><path d="M1 4h3l8-3v11l-8-3H1z"/><path d="M4 9l1 3h2l-1-3"/></svg>
      <span>New price is ready</span>
      <svg class="close" width="15" height="15" viewBox="0 0 15 15" stroke="#fff" stroke-width="2"><path d="M1 1l13 13M14 1L1 14"/></svg>
    </div>

    <nav class="nav">
      <div class="logo"><span class="dot"></span><span class="name">NimbusOps</span></div>
      <ul>
        <li>Product</li><li>Pricing</li><li>Solutions</li><li>Resources</li><li>About</li><li>Contact</li>
      </ul>
      <svg class="search" width="15" height="15" viewBox="0 0 15 15" fill="none" stroke="#fff" stroke-width="1.6"><circle cx="6.5" cy="6.5" r="5"/><path d="M10.2 10.2L14 14"/></svg>
      <span class="btn btn-solid">Contact Us</span>
    </nav>

    <h2 class="hero-title">A groundbreaking way for your small business to benefit from the power of the cloud</h2>
    <p class="hero-lead">NimbusOps as a Service is here to help small businesses utilise the power of the cloud without complicated set ups or scary price tags.</p>
    <p class="hero-text">Ready to modernise your infrastructure with a fully managed private cloud solution from NOaaS?</p>
    <div class="hero-actions">
      <span class="btn btn-solid">Contact Us</span>
      <span class="btn btn-ghost">Learn More</span>
    </div>

    <div class="hero-illustration" role="img" aria-label="Isometric illustration of a server stack linked to a cloud, laptop, phone and smartwatch"></div>

    <div class="chat">
      <svg width="22" height="20" viewBox="0 0 22 20" fill="none" stroke="#fff" stroke-width="1.6"><path d="M11 2c5 0 9 3 9 7s-4 7-9 7c-1 0-2 0-3-.3L3 18l1.3-3.6C2.8 13 2 11 2 9c0-4 4-7 9-7z"/><circle cx="7" cy="9" r=".8" fill="#fff"/><circle cx="11" cy="9" r=".8" fill="#fff"/><circle cx="15" cy="9" r=".8" fill="#fff"/></svg>
    </div>
  </section>
</div>
</body>
</html>
```